Identity Card Document Design

Looking for high quality identity card designs for templates.
Please read the detailed brief document which has sample designs and loads of info.
Instant Rejections :
1 You must NOT make anything illegal - anything which looks identical to an existing document. Create an ID card design entirely from scratch. Read the document for more info.
2 The artwork *has* to be provided as per the artwork specs in the document, as a print ready PDF to our size requirements.
3 No gen AI rubbish, don't waste your time, don't waste ours.
Question : In the document, there are certain letters which spell out a specific thing - what is this word? Please submit this word with your design.

```html
<!DOCTYPE html>
<html lang="en">
<head>
<meta charset="utf-8">
<title>Identity Card</title>
<link rel="stylesheet" href="https://fonts.googleapis.com/css2?family=Inter:ital,wght@0,500;1,400&family=IBM+Plex+Mono:wght@500&display=swap">
<style>
  :root {
    --page: #ffffff;
    --ink: #1c1c1f;
    --sky: #dbe8f7;
    --blush: #f8e1e6;
    --lavender: #dcdcf1;
    --band-bottom: #c9def4;
    --rose: #f3bcc8;
    --photo-light: #d9c2a6;
    --photo-dark: #8d6e52;
  }
  * { margin: 0; padding: 0; box-sizing: border-box; }
  html, body {
    width: 1200px;
    height: 790px;
    overflow: hidden;
    background: var(--page);
  }
  .id-card {
    position: absolute;
    left: 19px;
    top: 19px;
    width: 1162px;
    height: 751px;
    overflow: hidden;
    background: linear-gradient(180deg, var(--sky) 0%, var(--blush) 45%, var(--blush) 64%, var(--lavender) 64%, var(--lavender) 80%, var(--band-bottom) 100%);
    font-family: "Inter", Arial, sans-serif;
    color: var(--ink);
  }
  .security-pattern {
    position: absolute;
    inset: 0;
    background:
      radial-gradient(circle at 936px 375px, rgba(243,188,200,0.75) 0, rgba(243,188,200,0) 180px),
      radial-gradient(circle at 340px 330px, rgba(243,188,200,0.45) 0, rgba(243,188,200,0) 200px);
  }
  .field-label {
    position: absolute;
    font-style: italic;
    font-weight: 400;
    font-size: 24px;
    letter-spacing: 0.3px;
    line-height: 1;
  }
  .field-value {
    position: absolute;
    font-weight: 500;
    font-size: 40px;
    line-height: 45px;
    letter-spacing: 0.3px;
  }
  .col-left { left: 64px; }
  .col-right { left: 450px; }
  .portrait {
    position: absolute;
    left: 830px;
    top: 47px;
    width: 211px;
    height: 264px;
    background: linear-gradient(180deg, var(--photo-dark) 0%, var(--photo-light) 55%, #ecd9c8 100%);
    opacity: 0.85;
  }
  .mrz {
    position: absolute;
    left: 64px;
    font-family: "IBM Plex Mono", "Courier New", monospace;
    font-weight: 500;
    font-size: 46px;
    letter-spacing: 5.8px;
    line-height: 1;
    white-space: pre;
  }
</style>
</head>
<body>
  <main class="id-card">
    <div class="security-pattern" role="img" aria-label="Fine guilloche security pattern with rosettes"></div>

    <span class="field-label col-left" style="top:52px">SURNAME</span>
    <span class="field-value col-left" style="top:85px">MARLOWE</span>

    <span class="field-label col-left" style="top:146px">PLACE OF BIRTH</span>
    <span class="field-value col-left" style="top:179px">ADELAIDE</span>

    <span class="field-label col-left" style="top:242px">ADDRESS</span>
    <p class="field-value col-left" style="top:275px">14 FERN LANE,<br>SURRY HILLS,<br>NEW SOUTH WALES,<br>POSTCODE, AUSTRALIA</p>

    <span class="field-label col-right" style="top:52px">HEIGHT</span>
    <span class="field-value col-right" style="top:85px">163</span>

    <span class="field-label col-right" style="top:146px">COLOR OF EYES</span>
    <span class="field-value col-right" style="top:179px">GREY</span>

    <span class="field-label col-right" style="top:242px">DATE OF ISSUE</span>
    <span class="field-value col-right" style="top:275px">25/02/2025</span>

    <div class="portrait" role="img" aria-label="Portrait photograph of the card holder"></div>

    <div class="mrz" style="top:536px">IDAUS000000000272&lt;&lt;&lt;&lt;&lt;&lt;&lt;&lt;&lt;&lt;&lt;&lt;</div>
    <div class="mrz" style="top:596px">9306273F1510212AUS&lt;&lt;&lt;&lt;&lt;&lt;&lt;&lt;&lt;&lt;2</div>
    <div class="mrz" style="top:656px">CITIZEN&lt;&lt;HARPER&lt;&lt;MARLOWE&lt;&lt;&lt;&lt;&lt;</div>
  </main>
</body>
</html>
```